Healthy Lifestyle Vitamin Supplement Company needs a web site designed.

We are starting a new website for selling quality natural vitamins and supplements online plus providing news and information on healthy living. We DO NOT need any programming done for this site. Just the design in a layered photoshop file. This site needs to communicate that we are the authoritative source for healthy living and a trusted place to buy supplements and information on living a healthy lifestyle.

Triggers On page will be

Trigger set 1
Home - Shop By Brand - Top Sellers - Clearance - Help Center - My Favorites

Trigger set 2
Vitamins and Herbs - Natural Living - Aromatherapy - Coffee and Tea - Health and Beauty - Healthy Foods - Pet Health - Sports and Diet

Triggers Other
Login - Shopping Cart - Checkout - Track Order

Need a search bar in the design

Left side should be categories look at Verolane.com for example of categories.

Name and domain name is Brisk Meadow Crest

Will also need a logo to go along with that.

```html
<!DOCTYPE html>
<html lang="en">
<head>
<meta charset="utf-8">
<title>Brisk Meadow Crest</title>
<link href="https://fonts.googleapis.com/css2?family=Cabin:wght@400;500;600&family=Oswald:wght@500;600&display=swap" rel="stylesheet">
<style>
:root{
  --bar:#6b5f55;
  --bar-dark:#5b5148;
  --sub:#5d5249;
  --teal:#17ab97;
  --yellow:#f6b31a;
  --orange:#f26a31;
  --green:#2db34f;
  --text:#5a5a5a;
  --light:#efefef;
  --line:#e3e3e3;
  --white:#fff;
}
*{margin:0;padding:0;box-sizing:border-box}
html,body{width:775px;height:1200px;overflow:hidden;background:var(--white);font-family:"Cabin",sans-serif;color:var(--text)}
.page{position:relative;width:775px;height:1200px}
.abs{position:absolute}
.topbar{left:0;top:0;width:775px;height:27px;background:var(--bar);color:var(--white);font-size:10px}
.phone{left:128px;top:7px;font-size:11px;display:flex;align-items:center;gap:4px}
.toplinks{left:454px;top:8px;font-size:8px;display:flex;gap:6px}
.login{left:608px;top:6px;width:40px;height:15px;background:var(--green);font-size:8px;text-align:center;line-height:15px;border-radius:2px}
.logo{left:127px;top:43px;display:flex;align-items:center;gap:6px;font-size:20px;font-weight:600;color:var(--orange)}
.logo .dot{width:12px;height:12px;border-radius:50%;background:var(--green)}
.search{left:360px;top:46px;width:234px;height:26px;background:var(--light);border:1px solid var(--line);font-size:7px;color:#aaa;padding:9px 8px}
.search-btn{left:594px;top:46px;width:54px;height:26px;background:var(--green);color:var(--white);font-size:8px;text-align:center;line-height:26px}
.mainnav{left:127px;top:85px;width:521px;height:37px;background:var(--teal);display:flex;font-size:10px;color:var(--white)}
.mainnav span{padding:0 6px;line-height:37px}
.mainnav .home{background:var(--yellow);width:59px;text-align:center;margin-right:0}
.subnav{left:127px;top:122px;width:521px;height:28px;background:var(--sub);display:flex;color:var(--white);font-size:7.4px}
.subnav span{line-height:28px;padding:0 4.6px;border-right:1px solid #4a4139}
.subnav span:last-child{border:0}
.promo{left:127px;top:164px;width:117px;height:99px;background:linear-gradient(135deg,#f4f0f4,#c9c6cc 60%,#d44a8e)}
.news-h{left:127px;top:271px;width:117px;height:28px;background:var(--teal);color:var(--white);font-size:7.4px;font-weight:600;padding:11px 6px}
.news-b{left:127px;top:299px;width:117px;height:72px;background:var(--light);font-size:7.4px;padding:5px 7px;line-height:1.4}
.news-b .field{margin-top:6px;background:var(--white);height:15px;font-size:6px;color:#aaa;padding:4px 4px}
.news-b .btn{display:inline-block;margin-top:6px;background:var(--yellow);color:var(--white);font-size:7px;padding:2px 7px}
.hero-panel{left:262px;top:164px;width:118px;height:206px;background:var(--orange);font-family:"Oswald",sans-serif;color:var(--white);padding:16px 10px;line-height:1}
.hero-panel .a{font-size:13px;color:var(--yellow)}
.hero-panel .b{font-size:30px}
.hero-panel .c{font-size:30px;color:#5a4a40}
.hero-panel .d{font-size:17px}
.hero-panel .learn{margin-top:10px;background:var(--green);font-size:11px;text-align:center;padding:4px 0;width:97px}
.hero-photo{left:380px;top:164px;width:268px;height:206px;background:radial-gradient(circle at 70% 45%,#e9c8ae,#f3ece6 45%,#fbfbfa)}
.arrows{display:flex;gap:2px}
.arrows i{width:15px;height:10px;background:#3d3d3d;display:block}
.cat-h{left:127px;top:393px;width:117px;height:29px;background:var(--teal);color:var(--white);font-size:8px;font-weight:600;padding:10px 10px}
.cats{left:127px;top:422px;width:117px;height:429px;background:var(--bar);list-style:none;color:var(--white);font-size:7.4px}
.cats li{height:20.25px;line-height:20.25px;padding-left:19px;border-bottom:1px solid #5d5249;position:relative}
.cats li::before{content:"";position:absolute;left:9px;top:7px;border-left:3px solid var(--white);border-top:3px solid transparent;border-bottom:3px solid transparent}
.cats .more{color:var(--teal);border:0;text-align:center;padding:0;font-size:7.4px}
.cats .more::before{display:none}
.viewed-h{left:127px;top:871px;width:117px;height:28px;background:var(--teal);color:var(--white);font-size:8px;font-weight:600;padding:10px 11px}
.viewed{left:127px;top:899px;width:117px;height:95px;background:linear-gradient(#6e5b40,#3f3428);text-align:center;color:var(--white);font-size:6.4px;padding-top:35px}
.viewed .t{color:var(--teal);font-size:7.4px}
.viewed .btn{display:inline-block;background:var(--orange);padding:2px 4px;margin-top:4px}
.sec-h{font-size:8px;color:#666;letter-spacing:.2px}
.pager{display:flex;gap:7px;font-size:10px;color:#333}
.card{width:118px}
.card .img{height:106px;border:1px solid var(--line)}
.card p{font-size:7.3px;line-height:1.4;margin-top:4px}
.card .price{font-size:14px;margin-top:3px;color:#555}
.card .buy{display:inline-block;margin-top:3px;background:var(--orange);color:var(--white);font-size:7.4px;padding:1px 5px}
.card .buy.dark{background:#555}
.footer{left:0;top:1019px;width:775px;height:145px;background:var(--bar);color:var(--white);font-size:7.4px}
.col{position:absolute;top:27px;line-height:16.6px}
.icons{display:flex;gap:9px;margin-top:6px}
.icons i{width:15px;height:15px;background:var(--white);border-radius:2px;display:block}
.cards{display:flex;gap:6px;margin-top:6px}
.cards i{width:13px;height:8px;background:#d8d8d8;display:block}
.bottom{left:0;top:1164px;width:775px;height:36px;background:var(--bar-dark);color:var(--white);font-size:7.4px;text-align:center;line-height:36px}
</style>
</head>
<body>
<div class="page">
  <header class="abs topbar">
    <div class="abs phone"><svg width="9" height="9" viewBox="0 0 24 24"><path fill="#2db34f" d="M6.6 10.8a15 15 0 006.6 6.6l2.2-2.2a1 1 0 011-.25 11.4 11.4 0 003.6.57 1 1 0 011 1V20a1 1 0 01-1 1A17 17 0 013 4a1 1 0 011-1h3.5a1 1 0 011 1 11.4 11.4 0 00.57 3.6 1 1 0 01-.25 1z"/></svg>1-800-555-0142</div>
    <div class="abs toplinks"><span>Shopping Cart</span><span>|</span><span>Checkout</span><span>|</span><span>Track Order</span></div>
    <div class="abs login">LOGIN</div>
  </header>

  <div class="abs logo"><span class="dot"></span>Brisk Meadow Crest</div>
  <div class="abs search">Search Products</div>
  <div class="abs search-btn">SEARCH</div>

  <nav class="abs mainnav"><span class="home">Home</span><span>Shop By Brand</span><span>Top Sellers</span><span>Clearance</span><span>Help Center</span><span>My Favorites</span></nav>
  <nav class="abs subnav"><span>Vitamins and Herbs</span><span>Natural Living</span><span>Aromatherapy</span><span>Coffee and Tea</span><span>Health and Beauty</span><span>Healthy Foods</span><span>Pet Health</span><span>Sports and Diet</span></nav>

  <div class="abs promo" role="img" aria-label="Promotion for a women's complete multivitamin with a product bottle"></div>
  <div class="abs news-h">SUBSCRIBE FOR NEWSLETTER</div>
  <div class="abs news-b">Lorem Ipsum is simply dummy text of the printing<div class="field">Enter Your E-Mail ID</div><span class="btn">SUBSCRIBE</span></div>

  <div class="abs hero-panel"><div class="a">WE ARE A SELLING</div><div class="b">QUALITY</div><div class="c">NATURAL</div><div class="b">VITAMINS</div><div class="d">&amp;SUPPLEMENTS</div><div class="learn">LEARN MORE</div></div>
  <div class="abs hero-photo" role="img" aria-label="Woman eating a fresh salad"></div>
  <div class="abs arrows" style="left:605px;top:351px"><i></i><i></i></div>

  <div class="abs cat-h">CATEGORIES</div>
  <ul class="abs cats">
    <li>A &amp; D Vitamins</li><li>Acidophilus/Probiotics</li><li>Amino Acid Supplements</li><li>Antioxidants</li><li>B Vitamins</li><li>B-12 Vitamins</li><li>B-Complex Vitamins</li><li>Babies &amp; Kids newtag</li><li>C Vitamins</li><li>Calcium Supplements</li><li>Co Q-10</li><li>D Vitamins</li><li>Diet &amp; Lifestyle</li><li>Digestive Health</li><li>E Vitamins</li><li>Eye Health</li><li>Fish Oils</li><li>Garcinia Cambogia</li><li>Health &amp; Beauty</li><li>Herbal Supplements</li><li class="more">MORE CATEGORIES ⊕</li>
  </ul>
  <div class="abs viewed-h">VIEWED PRODUCTS</div>
  <div class="abs viewed" role="img" aria-label="Viewed product with green herbs"><div class="t">NEQUE PORRO QUISQUAM</div>There is no one who loves pain<br>itself, who seeks after<br><span class="btn">VIEW DETAILS</span></div>

  <div class="abs sec-h" style="left:262px;top:403px">FEATURED PRODUCTS</div>
  <div class="abs pager" style="left:632px;top:400px"><span>‹</span><span>›</span></div>
  <div class="abs card" style="left:262px;top:424px"><div class="img" role="img" aria-label="Supplement bottles" style="background:linear-gradient(#eee,#9a9a9a)"></div><p>Lorem Ipsum is simply dummy text of the printing .</p><div class="price">$28.00</div><span class="buy dark">BUY NOW</span></div>
  <div class="abs card" style="left:395px;top:424px"><div class="img" role="img" aria-label="Vitamin C bottles" style="background:radial-gradient(circle at 55% 60%,#d8823a,#f6f2ee 60%)"></div><p>Lorem Ipsum is simply dummy text of the printing .</p><div class="price">$28.00</div><span class="buy">BUY NOW</span></div>
  <div class="abs card" style="left:530px;top:424px"><div class="img" role="img" aria-label="Amber bottle with softgels" style="background:radial-gradient(circle at 50% 45%,#7a3f1c,#fafafa 55%)"></div><p>Lorem Ipsum is simply dummy text of the printing .</p><div class="price">$28.00</div><span class="buy">BUY NOW</span></div>

  <div class="abs sec-h" style="left:262px;top:614px">PRODUCTS</div>
  <div class="abs pager" style="left:632px;top:611px"><span>‹</span><span>›</span></div>
  <div class="abs card" style="left:262px;top:636px"><div class="img" role="img" aria-label="Spilled white pills" style="background:radial-gradient(circle at 60% 65%,#8a8a8a,#fafafa 50%)"></div><p>Lorem Ipsum is simply dummy text of the printing .</p><div class="price">$28.00</div><span class="buy dark">BUY NOW</span></div>
  <div class="abs card" style="left:395px;top:636px"><div class="img" role="img" aria-label="Herbal capsules with wooden scoop" style="background:radial-gradient(circle at 55% 60%,#b58660,#fafafa 55%)"></div><p>Lorem Ipsum is simply dummy text of the printing .</p><div class="price">$28.00</div><span class="buy">BUY NOW</span></div>
  <div class="abs card" style="left:530px;top:636px"><div class="img" role="img" aria-label="Green herbal capsules with leaves" style="background:radial-gradient(circle at 50% 55%,#8aa43a,#fafafa 55%)"></div><p>Lorem Ipsum is simply dummy text of the printing .</p><div class="price">$28.00</div><span class="buy">BUY NOW</span></div>
  <div class="abs card" style="left:262px;top:821px"><div class="img" role="img" aria-label="Amber bottle spilling capsules" style="background:radial-gradient(circle at 45% 50%,#9a5a24,#fafafa 60%)"></div><p>Lorem Ipsum is simply dummy text of the printing .</p><div class="price">$28.00</div><span class="buy">BUY NOW</span></div>
  <div class="abs card" style="left:395px;top:821px"><div class="img" role="img" aria-label="Mortar with herbs and pills" style="background:radial-gradient(circle at 50% 60%,#c6b48a,#fafafa 55%)"></div><p>Lorem Ipsum is simply dummy text of the printing .</p><div class="price">$28.00</div><span class="buy">BUY NOW</span></div>
  <div class="abs card" style="left:530px;top:821px"><div class="img" role="img" aria-label="Amber jar of capsules with leaves" style="background:radial-gradient(circle at 60% 50%,#7b3e18,#fafafa 58%)"></div><p>Lorem Ipsum is simply dummy text of the printing .</p><div class="price">$28.00</div><span class="buy">BUY NOW</span></div>

  <footer class="abs footer">
    <div class="col" style="left:127px">Home<br>Shop By Brand<br>Top Sellers<br>Clearance<br>Help Center<br>My Favorites</div>
    <div class="col" style="left:217px">My Account<br>Log In<br>Create Account<br>My Favorites<br>Order History<br>Track Order</div>
    <div class="col" style="left:307px">Customer Service<br>Price Match Guarantee<br>Coupon Policy<br>Help Center<br>Affiliate Program<br>Contact Us<br>Quality Guarantee</div>
    <div class="col" style="left:424px">Shipping &amp; Returns<br>International Shipping<br>Lost or Damaged<br>Return Policy<br>Shipping Information</div>
    <div class="col" style="left:530px">Connect With Us<div class="icons"><i></i><i></i><i></i><i></i><i></i></div><div style="margin-top:6px">Payment With Us</div><div class="cards"><i></i><i></i><i></i><i></i><i></i></div></div>
  </footer>
  <div class="abs bottom">© 2014 Company Name ,All Rights Reserved</div>
</div>
</body>
</html>
```